menu board design: harbor burger

we are a burger restaurant.
we need to re design our menu board to fit within the new design of the restaurant. we are after something simple and easy to read. the overall look and feel of the design should be inline with the design of the shop.

Target Market(s)

18-40 male and female

Colors

Designer to choose colors to be used in the design.

Requirements
Must have
• easy to read. good layout. white background. branding included in design.

```html
<!DOCTYPE html>
<html lang="en">
<head>
<meta charset="utf-8">
<title>Harbor Burger – Menu Board</title>
<link rel="stylesheet" href="https://fonts.googleapis.com/css2?family=Montserrat:wght@300;400;500;600;700&display=swap">
<style>
  :root{
    --brand-blue:#1f4f9a;
    --bar-yellow:#f0d75c;
    --title-gold:#e6c412;
    --text-blue:#6f83b9;
    --band-grey:#e7ebef;
    --soft-yellow:#fbf0b8;
    --muted-grey:#98a3b4;
    --white:#ffffff;
  }
  *{box-sizing:border-box;margin:0;padding:0}
  html,body{width:1200px;height:600px;overflow:hidden}
  body{background:var(--brand-blue);font-family:"Montserrat",sans-serif;color:var(--text-blue)}
  .board{position:relative;width:1200px;height:600px;background:var(--brand-blue)}
  .panel{position:absolute;top:0;height:576px;background:var(--white)}
  .panel--brand{left:24px;width:233px}
  .panel--beef{left:274px;width:316px}
  .panel--chicken{left:609px;width:316px}
  .panel--sides{left:943px;width:234px}
  .tab{position:absolute;top:0;height:16px;width:139px}
  .tab--gold{background:var(--title-gold)}
  .tab--blue{background:var(--brand-blue)}

  /* brand panel */
  .brand-name{position:absolute;left:0;right:0;top:226px;text-align:center;font-weight:700;font-size:34px;line-height:1.05;color:var(--brand-blue);text-transform:uppercase;letter-spacing:1px}
  .brand-tagline{position:absolute;left:0;right:0;top:372px;text-align:center;font-size:11px;letter-spacing:3px;color:var(--brand-blue)}

  /* headings */
  .panel-title{position:absolute;left:0;right:0;top:38px;text-align:center;font-weight:300;line-height:.88}
  .panel-title .top{display:block;font-size:40px;color:var(--title-gold)}
  .panel-title .bottom{display:block;font-size:41px;color:var(--brand-blue)}
  .panel-title--single{top:70px}
  .panel-title--single .top{font-size:44px}
  .intro{position:absolute;left:0;right:0;top:127px;height:48px;background:var(--band-grey);display:flex;align-items:center;justify-content:center;text-align:center;font-size:8.4px;line-height:1.75;color:var(--brand-blue);padding:0 30px}
  .upsell{position:absolute;left:0;right:0;top:195px;text-align:center;font-weight:700;font-size:14px;letter-spacing:3.2px;color:var(--muted-grey)}

  /* menu item bar */
  .item{position:absolute;left:0;right:0}
  .bar{display:flex;align-items:stretch;height:17px;background:var(--bar-yellow);margin-right:19px}
  .bar .mark{width:21px;background:var(--brand-blue);display:flex;align-items:center;justify-content:center}
  .bar .mark svg{width:10px;height:10px}
  .bar .name{flex:1;padding-left:13px;font-weight:600;font-size:12.5px;line-height:17px;color:var(--brand-blue);letter-spacing:.3px}
  .bar .price{width:26px;background:var(--brand-blue);color:var(--white);font-size:11px;line-height:17px;text-align:center}
  .bar--flush{margin-right:0}
  .desc{padding:5px 40px 0 34px;font-size:9.2px;line-height:1.25;text-transform:uppercase;color:var(--text-blue)}

  /* sides */
  .side-desc{position:absolute;left:0;right:0;text-align:center;font-size:7.6px;line-height:1.45;text-transform:uppercase;color:var(--text-blue)}
  .section-head{position:absolute;left:0;right:0;height:26px;background:var(--bar-yellow);display:flex;align-items:center}
  .section-head .mark{width:21px;height:100%;background:var(--brand-blue);display:flex;align-items:center;justify-content:center}
  .section-head .mark svg{width:10px;height:10px}
  .section-head .label{flex:1;text-align:center;font-size:13.5px;color:var(--brand-blue);font-weight:500}
  .steps{position:absolute;left:0;right:0;top:246px;height:164px;background:var(--band-grey)}
  .step-title{position:absolute;left:25px;font-weight:700;font-size:10.5px;color:var(--title-gold)}
  .step-note{position:absolute;left:25px;font-size:9.5px;color:var(--text-blue)}
  .choice{position:absolute;left:0;right:0;height:15px;background:var(--soft-yellow);display:flex;align-items:center;padding-left:25px;font-size:8.8px;color:var(--text-blue);border-top:1px solid #f6e596}
  .choice .price{margin-left:auto;width:21px;height:100%;background:var(--brand-blue);color:var(--white);font-size:8.5px;display:flex;align-items:center;justify-content:center;margin-right:11px}
  .option{position:absolute;left:0;right:0;background:var(--soft-yellow);padding:2px 10px 2px 25px;font-size:8.6px;line-height:1.3;color:var(--text-blue)}
  .option b{color:var(--brand-blue)}
  .ribs-table{position:absolute;left:0;right:0;top:504px;height:47px;background:var(--soft-yellow);display:flex}
  .ribs-rows{width:119px;display:flex;flex-direction:column}
  .ribs-rows .row{flex:1;display:flex;align-items:center;border-bottom:1px solid #f6e596}
  .ribs-rows .size{flex:1;text-align:center;font-size:9px;color:var(--text-blue)}
  .ribs-rows .price{width:26px;height:100%;background:var(--brand-blue);color:var(--white);font-size:8.5px;display:flex;align-items:center;justify-content:center}
  .ribs-sauces{flex:1;display:flex;align-items:center;justify-content:center;text-align:center;font-weight:700;font-size:8.5px;line-height:1.3;color:var(--brand-blue);text-transform:uppercase}
</style>
</head>
<body>
<svg width="0" height="0" style="position:absolute">
  <defs>
    <symbol id="star" viewBox="0 0 24 24"><path d="M12 2l2.9 6.6 7.1.6-5.4 4.7 1.6 7-6.2-3.7-6.2 3.7 1.6-7L2 9.2l7.1-.6z" fill="#e6c412"/></symbol>
  </defs>
</svg>
<main class="board">

  <section class="panel panel--brand">
    <div class="tab tab--gold" style="left:53px"></div>
    <h1 class="brand-name">Harbor<br>Burger</h1>
    <p class="brand-tagline">FRESH OFF THE GRILL</p>
  </section>

  <section class="panel panel--beef">
    <div class="tab tab--blue" style="left:103px"></div>
    <h2 class="panel-title"><span class="top">Beef</span><span class="bottom">Burgers</span></h2>
    <p class="intro">ALL OUR PATTIES ARE 100% NATURAL BEEF. WE KNOW BECAUSE WE GRIND IT OURSELVES. SMASHED YO ORDER ON A HOT GRILL RITE IN FRONT YOU.</p>
    <p class="upsell">DOUBLE PATTY &nbsp;ADD 4</p>
    <div class="item" style="top:231px">
      <div class="bar"><span class="mark"><svg><use href="#star"/></svg></span><span class="name">CLASSIC BEEF</span><span class="price">8.9</span></div>
      <p class="desc">Shredded lettuce, sliced tomatoes, caramelized unions, beetroot and BBQ sauce on a buttered sesame seed bun.</p>
    </div>
    <div class="item" style="top:298px">
      <div class="bar"><span class="mark"><svg><use href="#star"/></svg></span><span class="name">CHEESE BURGER</span><span class="price">9.5</span></div>
      <p class="desc">Dill pickles, minced union, American cheese, mustard and ketchup on a soft milk bun.</p>
    </div>
    <div class="item" style="top:365px">
      <div class="bar"><span class="mark"><svg><use href="#star"/></svg></span><span class="name">FLAME GRILL</span><span class="price">9.5</span></div>
      <p class="desc">Shredded lettuce, sliced tomato, minced union, dill pickles, American cheese, mayo and ketchup on a soft milk bun.</p>
    </div>
    <div class="item" style="top:432px">
      <div class="bar"><span class="mark"><svg><use href="#star"/></svg></span><span class="name">BIG MIC</span><span class="price">9.9</span></div>
      <p class="desc">Shredded lettuce, dill pickles, minced union, American cheese and special sauce on a soft milk bun.</p>
    </div>
    <div class="item" style="top:499px">
      <div class="bar"><span class="mark"><svg><use href="#star"/></svg></span><span class="name">TRUFFLED</span><span class="price">9.9</span></div>
      <p class="desc">Rocket, caramelized union, dill pickles, havarti cheese and truffle infused mayo on a soft milk bun.</p>
    </div>
  </section>

  <section class="panel panel--chicken">
    <div class="tab tab--gold" style="left:89px"></div>
    <h2 class="panel-title"><span class="top">Chicken</span><span class="bottom">Burgers</span></h2>
    <p class="intro">ALL OUR BURGER PATTIES ARE PREPARED ONSITE DAILY USING PREMIUM QUALITY CHICKEN BREAST.</p>
    <p class="upsell">DOUBLE PATTY ADD 4</p>
    <div class="item" style="top:231px">
      <div class="bar"><span class="mark"><svg><use href="#star"/></svg></span><span class="name">CLASSIC CHICKEN</span><span class="price">8.9</span></div>
      <p class="desc">Shredded lettuce, cheese and mayo on a classic sesame seed bun.</p>
    </div>
    <div class="item" style="top:291px">
      <div class="bar"><span class="mark"><svg><use href="#star"/></svg></span><span class="name">PIRRI PIRRI</span><span class="price">9.5</span></div>
      <p class="desc">Shredded lettuce, cheese, mayo and house made pirri pirri on a classic sesame seed bun.</p>
    </div>
    <div class="item" style="top:362px">
      <div class="bar"><span class="mark"><svg><use href="#star"/></svg></span><span class="name">KENTUCKY</span><span class="price">9.9</span></div>
      <p class="desc">Shredded lettuce, swiss cheese, and feisty mayo on a soft milk bun.</p>
    </div>
    <div class="item" style="top:422px">
      <div class="bar"><span class="mark"><svg><use href="#star"/></svg></span><span class="name">EL BURGER</span><span class="price">9.9</span></div>
      <p class="desc">Shredded lettuce, salsa, guacamole, cheese and chipotle mayo on a classic sesame seed bun.</p>
    </div>
  </section>

  <section class="panel panel--sides">
    <div class="tab tab--blue" style="left:41px"></div>
    <h2 class="panel-title panel-title--single"><span class="top">Sides</span></h2>
    <div class="item" style="top:128px">
      <div class="bar bar--flush"><span class="mark"><svg><use href="#star"/></svg></span><span class="name" style="padding-left:5px">FRIES</span><span class="price">3.5</span></div>
    </div>
    <div class="item" style="top:154px">
      <div class="bar bar--flush"><span class="mark"><svg><use href="#star"/></svg></span><span class="name" style="padding-left:5px">KENTUCKY TENDERS</span><span class="price">6.9</span></div>
    </div>
    <p class="side-desc" style="top:176px">Breaded and fried chicken tenders<br>with secret seasoning. <b style="color:var(--brand-blue)">(2 PCS)</b></p>

    <div class="section-head" style="top:220px"><span class="mark"><svg><use href="#star"/></svg></span><span class="label">NACHOS &amp; LOADED FRIES</span></div>
    <div class="steps">
      <p class="step-title" style="top:7px">STEP ONE</p>
      <p class="step-note" style="top:20px">CHOOSE EITHER,</p>
      <div class="choice" style="top:34px">Seasoned Fries<span class="price">9.9</span></div>
      <div class="choice" style="top:50px">Or Freshly cooked corn chips<span class="price">11.5</span></div>
      <p class="step-title" style="top:79px">STEP TWO:</p>
      <p class="step-note" style="top:92px">CHOOSE ONE,</p>
      <p class="option" style="top:106px"><b>Guacamole</b> Salsa fresca, guacamole, jalapeños, ches and sour cream.</p>
      <p class="option" style="top:133px"><b>Beef Chilli</b> Salsa fresca, beef chilli, jalapeños, ches sauce and sour cream.</p>
    </div>

    <div class="section-head" style="top:421px;height:28px"><span class="mark"><svg><use href="#star"/></svg></span><span class="label">BUFFALO CHICKEN RIBS</span></div>
    <p class="side-desc" style="top:455px">Buffalo style fried chicken ribs<br>smothered in one of our<br>mouth-watering sauces,<br>served with a side of ranche sauce.</p>
    <div class="ribs-table">
      <div class="ribs-rows">
        <div class="row"><span class="size">6 PACK</span><span class="price">6.9</span></div>
        <div class="row"><span class="size">12 PACK</span><span class="price">12.9</span></div>
        <div class="row"><span class="size">24 PACK</span><span class="price">23.9</span></div>
      </div>
      <p class="ribs-sauces">Classic<br>hot sauce<br>or smoky<br>BBQ.</p>
    </div>
  </section>

</main>
</body>
</html>
```